Business Cards and Stationery for Mobile Ultrasound
Redfern Harbor Mobile Ultrasound
Business Cards and Stationery for Mobile Ultrasound - Medical
Creative Brief
Professional
Marovic Deltrane
P.O Box 827 Quenton CA 95871
mar@rhqx.example
rhqx.example

```html
<!DOCTYPE html>
<html lang="en">
<head>
<meta charset="utf-8">
<title>Redfern Harbor Mobile Ultrasound — Business Card</title>
<link rel="stylesheet" href="https://fonts.googleapis.com/css2?family=Cinzel:wght@400&family=Tinos:wght@400;700&display=swap">
<style>
  :root {
    --stage: #3b3b3d;
    --stage-edge: #252527;
    --purple-deep: #3a0f78;
    --purple: #5a1fa6;
    --purple-light: #7b3cc9;
    --green: #3c9a2c;
    --green-light: #79c043;
    --paper: #ffffff;
    --ink: #4a4a4a;
  }
  * { box-sizing: border-box; margin: 0; padding: 0; }
  html, body { width: 1200px; height: 901px; overflow: hidden; }
  body {
    background: radial-gradient(ellipse at center, var(--stage) 0%, var(--stage-edge) 100%);
    font-family: "Tinos", "Times New Roman", serif;
    position: relative;
  }
  .card {
    position: absolute;
    left: 300px;
    width: 600px;
    height: 343px;
    border-radius: 4px;
    overflow: hidden;
    box-shadow: 0 14px 30px rgba(0,0,0,.45);
  }
  .card--front {
    top: 70px;
    background: radial-gradient(ellipse at center, var(--purple-light) 0%, var(--purple) 45%, var(--purple-deep) 100%);
    display: flex;
    align-items: center;
    justify-content: center;
  }
  .brand-name {
    font-family: "Tinos", "Times New Roman", serif;
    font-weight: 700;
    text-align: center;
    line-height: 1.1;
    display: flex;
    align-items: center;
    gap: 14px;
  }
  .brand-name__dot {
    width: 16px; height: 16px; border-radius: 50%;
    flex: none;
  }
  .card--front .brand-name { color: var(--paper); font-size: 34px; }
  .card--front .brand-name__dot { background: var(--paper); }

  .card--back { top: 488px; background: var(--paper); }
  .card__band { position: absolute; inset: 0; width: 600px; height: 343px; }
  .holder {
    position: absolute; left: 38px; top: 26px;
    color: var(--paper); font-size: 22px; font-weight: 400;
  }
  .contact {
    position: absolute; left: 34px; top: 148px;
    list-style: none; color: var(--ink); font-size: 14px; line-height: 1.35;
  }
  .contact li { display: flex; align-items: center; gap: 8px; min-height: 21px; }
  .contact .contact__address { padding-left: 24px; display: block; margin-bottom: 4px; }
  .contact svg { width: 16px; height: 16px; flex: none; }
  .card--back .brand-name {
    position: absolute; right: 36px; bottom: 44px;
    color: var(--purple); font-size: 27px; text-align: left;
  }
  .card--back .brand-name__dot { background: var(--green); }
</style>
</head>
<body>
  <section class="card card--front" aria-label="Card front">
    <div class="brand-name"><span class="brand-name__dot"></span><span>Redfern Harbor<br>Mobile Ultrasound</span></div>
  </section>

  <section class="card card--back" aria-label="Card back">
    <svg class="card__band" viewBox="0 0 600 343" preserveAspectRatio="none" aria-hidden="true">
      <defs>
        <linearGradient id="bandFill" x1="0" y1="0" x2="1" y2="1">
          <stop offset="0" stop-color="var(--purple-deep)"/>
          <stop offset=".6" stop-color="var(--purple)"/>
          <stop offset="1" stop-color="var(--purple-light)"/>
        </linearGradient>
      </defs>
      <path d="M0 0 H600 V140 C470 70 280 150 0 118 Z" fill="url(#bandFill)"/>
      <path d="M0 118 C280 150 470 70 600 140 V152 C470 86 280 166 0 132 Z" fill="var(--green)"/>
      <path d="M0 132 C280 166 470 86 600 152 V158 C470 96 280 174 0 138 Z" fill="var(--green-light)"/>
    </svg>

    <h1 class="holder">Marovic Deltrane</h1>

    <ul class="contact">
      <li class="contact__address">P.O Box 827<br>Quenton CA 95871</li>
      <li>
        <svg viewBox="0 0 16 16"><circle cx="8" cy="8" r="8" fill="var(--purple)"/><path d="M5 4.5c.5-.5 1.2-.3 1.5.2l.6 1.2c.2.4 0 .8-.3 1l-.4.3c.4 1 1.2 1.8 2.2 2.2l.3-.4c.3-.3.7-.4 1-.2l1.2.6c.5.3.6 1 .2 1.5-.6.7-1.6.9-2.5.5-1.9-.9-3.3-2.3-4.2-4.2-.4-.9-.2-1.9.4-2.7z" fill="#fff"/></svg>
        <span>5550148273</span>
      </li>
      <li>
        <svg viewBox="0 0 16 16"><circle cx="8" cy="8" r="8" fill="var(--purple)"/><rect x="4" y="5" width="8" height="6" rx="1" fill="#fff"/><path d="M4.3 5.4 8 8.4l3.7-3" stroke="var(--purple)" stroke-width="1" fill="none"/></svg>
        <span>mar@rhqx.example</span>
      </li>
      <li>
        <svg viewBox="0 0 16 16"><circle cx="8" cy="8" r="8" fill="var(--purple)"/><circle cx="8" cy="8" r="4" stroke="#fff" stroke-width="1" fill="none"/><path d="M4 8h8M8 4c-1.6 2.4-1.6 5.6 0 8M8 4c1.6 2.4 1.6 5.6 0 8" stroke="#fff" stroke-width=".8" fill="none"/></svg>
        <span>www.rhqx.example</span>
      </li>
    </ul>

    <div class="brand-name"><span class="brand-name__dot"></span><span>Redfern Harbor<br>Mobile Ultrasound</span></div>
  </section>
</body>
</html>
```